Redesign of Mailer for Salon Suite Company

Redesign an existing postcard for a new look/feel. Current design is a bit on the "masculine" side and our target audience is predominantly female. We rent individual salon rooms to hair stylists who want to work for themselves and run their own business, but still be in a professional salon space they share with other independent salon owners.

Color wise- use our logo orange, white, light blue.

Keep the location info and the mailing label white space on the back side and the print/cut margins as currently set.

The text items can be modified as needed. We probably have too much and want to err on the side of more visual, less text- but still getting some key points across.

A look and feel I like (from another salon suite company) is Tress Haven. I've attached a design of theirs that you can use for ideas. This web page also has some of their other print collateral that I like.

http://brinwellcreative.example/case_studies/tresshaven.html

Target Market(s)

Licensed cosmotologists who are ready to work for themselves instead of someone else.

Industry/Entity Type

Salon

Font styles to use
Sans Serif

Colors
fbca95
f78f20
ffffff
85cae6

Requirements
Must have
• Main Tagline/Message- attention getter- I like having the orange block with white text as done is some of the Tress Have designs- superimposed over a large image of a hair stylist. I'm in the process of getting some photos of our tenants taken and hope one will work- but for now, just use something stock.
• Back side has to have the white space for the mailing label and should list our 4 locations with pictures of each. I'm also getting new pictures of the 4 locations, but for now use the ones from our existing mailer design (attached).

```html
<!DOCTYPE html>
<html lang="en">
<head>
<meta charset="utf-8">
<title>Vela Salon Suites – Mailer Back</title>
<link href="https://fonts.googleapis.com/css2?family=Quicksand:wght@500;700&display=swap" rel="stylesheet">
<style>
  :root {
    --orange: #f78f20;
    --orange-soft: #fbca95;
    --white: #ffffff;
    --sky: #85cae6;
    --ink: #2a2a2a;
    --frame: #6b6b6b;
  }
  * { margin: 0; padding: 0; box-sizing: border-box; }
  html, body { width: 1200px; height: 773px; overflow: hidden; background: var(--white); }
  body { font-family: "Quicksand", "Helvetica Neue", Arial, sans-serif; font-weight: 500; color: var(--ink); }

  .mailer { position: relative; width: 1200px; height: 773px; background: var(--white); }

  .band-main { position: absolute; left: 0; top: 0; width: 797px; height: 672px; background: var(--orange); border-bottom: 6px solid var(--sky); }
  .band-contact { position: absolute; left: 797px; top: 0; width: 403px; height: 336px; background: var(--orange); border-bottom: 6px solid var(--sky); }

  /* Hero: stylist photo with tagline block */
  .hero { position: absolute; left: 24px; top: 24px; width: 287px; height: 318px; border-radius: 16px; overflow: hidden;
    background: linear-gradient(160deg, var(--sky) 0%, #cfe8f3 45%, var(--orange-soft) 100%); }
  .tagline { position: absolute; left: 0; bottom: 22px; width: 250px; padding: 14px 18px 16px;
    background: var(--orange); color: var(--white); border-radius: 0 14px 14px 0; }
  .tagline-main { display: block; font-weight: 700; font-size: 27px; line-height: 31px; }
  .tagline-sub { display: block; margin-top: 6px; font-weight: 500; font-size: 15px; line-height: 19px; }

  /* Advantage card */
  .advantage { position: absolute; left: 24px; top: 360px; width: 287px; height: 290px;
    background: var(--white); border-radius: 16px; padding: 20px 18px 0 20px; }
  .advantage-title { color: var(--orange); font-weight: 700; font-size: 23px; line-height: 28px; }
  .advantage-rule { width: 44px; height: 4px; border-radius: 2px; background: var(--sky); margin-top: 8px; }
  .advantage-list { list-style: none; margin-top: 14px; font-size: 14.5px; line-height: 23.5px; }
  .advantage-list li { position: relative; padding-left: 16px; }
  .advantage-list li::before { content: ""; position: absolute; left: 0; top: 8px; width: 7px; height: 7px; border-radius: 50%; background: var(--sky); }

  /* Locations */
  .location { position: absolute; left: 327px; width: 470px; height: 150px; }
  .location-photo { position: absolute; left: 0; top: 0; width: 253px; height: 150px; border-radius: 14px; }
  .photo-a { background: linear-gradient(to bottom, #a9d3ec 0%, #d6e6ef 45%, #9a7a64 62%, #6a625c 100%); }
  .photo-b { background: linear-gradient(to bottom, #85b9e3 0%, #c6dcec 40%, #e6d6b0 62%, #8a7a66 100%); }
  .photo-c { background: linear-gradient(to bottom, #8cc2e6 0%, #cfe0ec 32%, #a8583f 58%, #c4bfb8 100%); }
  .photo-d { background: linear-gradient(to bottom, #6a5a4e 0%, #9a765e 48%, #b6b1aa 100%); }
  .location-info { position: absolute; left: 271px; top: 40px; width: 190px; }
  .location-mark { width: 28px; height: 4px; border-radius: 2px; background: var(--sky); margin-bottom: 10px; }
  .location-name { display: block; color: var(--white); font-weight: 700; font-size: 20px; line-height: 25px; }
  .location-detail { display: block; font-size: 15px; line-height: 21px; }

  /* Contact side */
  .brand { position: absolute; left: 852px; top: 34px; color: var(--white); }
  .brand-name { display: block; font-weight: 700; font-size: 64px; line-height: 70px; }
  .brand-sub { display: block; margin-top: 4px; font-weight: 700; font-size: 12px; letter-spacing: 0.26em; }

  .stamp-box { position: absolute; left: 1013px; top: 22px; width: 158px; height: 167px; border: 1px solid var(--frame); border-radius: 6px; }

  .contact { position: absolute; left: 852px; top: 212px; width: 320px; }
  .contact-title { display: inline-block; background: var(--sky); color: var(--white); font-weight: 700;
    font-size: 19px; line-height: 30px; padding: 0 14px; border-radius: 15px; }
  .contact-lines { margin-top: 10px; padding-left: 4px; font-size: 17px; line-height: 24px; font-style: normal; }
</style>
</head>
<body>
<main class="mailer">
  <div class="band-main"></div>
  <div class="band-contact"></div>

  <section class="hero" role="img" aria-label="Photo of a hair stylist styling a client's hair in her own salon suite">
    <p class="tagline">
      <span class="tagline-main">Be your own boss.</span>
      <span class="tagline-sub">Your suite, your style, your salon.</span>
    </p>
  </section>

  <section class="advantage">
    <h2 class="advantage-title">The Vela Advantage</h2>
    <div class="advantage-rule"></div>
    <ul class="advantage-list">
      <li>Visible retail storefront locations</li>
      <li>Modern, stylish design</li>
      <li>New Business Setup Assistance</li>
      <li>Free utilities, Laundry and WiFi</li>
      <li>Flexible terms:<br>MTM, 6 Mo., 1 yr, 2 yr</li>
      <li>Generous start-up allowance</li>
      <li>Generous referral fees</li>
    </ul>
  </section>

  <section class="location" style="top:24px">
    <div class="location-photo photo-a" role="img" aria-label="Photo of the Junction Point retail storefront building in Tempe"></div>
    <div class="location-info"><div class="location-mark"></div><span class="location-name">Junction Point</span><span class="location-detail">Tempe</span><span class="location-detail">(Alder &amp; Birch)</span></div>
  </section>

  <section class="location" style="top:186px">
    <div class="location-photo photo-b" role="img" aria-label="Photo of the Linden Plaza storefront building in Gilbert"></div>
    <div class="location-info"><div class="location-mark"></div><span class="location-name">Linden Plaza</span><span class="location-detail">Gilbert</span><span class="location-detail">(Cedar &amp; Maple)</span></div>
  </section>

  <section class="location" style="top:348px">
    <div class="location-photo photo-c" role="img" aria-label="Photo of the Heritage Court stone and brick storefront in Mesa"></div>
    <div class="location-info"><div class="location-mark"></div><span class="location-name">Heritage Court</span><span class="location-detail">Mesa</span><span class="location-detail">(Willow &amp; Aspen)</span></div>
  </section>

  <section class="location" style="top:510px">
    <div class="location-photo photo-d" role="img" aria-label="Photo of the Sage Village storefront walkway in Mesa"></div>
    <div class="location-info"><div class="location-mark"></div><span class="location-name">Sage Village</span><span class="location-detail">Mesa</span><span class="location-detail">(Juniper &amp; Hollow)</span></div>
  </section>

  <div class="brand">
    <span class="brand-name">vela</span>
    <span class="brand-sub">SALON SUITES</span>
  </div>

  <div class="stamp-box" aria-label="Postage area"></div>

  <section class="contact">
    <h2 class="contact-title">Call for more details</h2>
    <address class="contact-lines">
      (480) 555-0147<br>
      info@velasuites.example<br>
      velasuites.example
    </address>
  </section>
</main>
</body>
</html>
```